Business Card for a mobile physiotherapy company

I need a layout for a business card for a mobile physiotherapy company.
Slogan is "Mobile Physiotherapy - Your Road To Recovery"
Phone number is 867-412-5093
Email VantePhysio@mailbox-demo.ca (subject to change with website)
Website www.VantePhysio.ca
My name and credentials: Gil Varney Gil Varney, BSc(kin), MPT, CAFCI, IMS
Information maybe included: Direct Billing, Services including Physiotherapy, IMS, acupuncture
Maybe include facebook and instagram logos
One side with the logo clean and sharp
Other side with details, try not to look too busy, keep everything concise

```html
<!DOCTYPE html>
<html lang="en">
<head>
<meta charset="utf-8">
<title>Vante Physio – Business Card</title>
<link href="https://fonts.googleapis.com/css2?family=Merriweather:wght@400;700&display=swap" rel="stylesheet">
<style>
  :root {
    --bg: #3a3a3c;
    --card: #1e1e20;
    --blue: #2b5889;
    --teal: #1f6a5c;
    --green: #2f7a58;
    --white: #f2f2f2;
    --muted: #c9d3dc;
  }
  * { box-sizing: border-box; margin: 0; padding: 0; }
  html, body { width: 799px; height: 1200px; overflow: hidden; }
  body {
    background: var(--bg);
    font-family: "Merriweather", Georgia, serif;
    color: var(--white);
    position: relative;
  }
  .card {
    position: absolute;
    left: 80px;
    width: 640px;
    height: 370px;
    background: var(--card);
    border-radius: 22px;
    overflow: hidden;
    box-shadow: 0 14px 30px rgba(0,0,0,.45);
  }
  .card--front { top: 110px; }
  .card--back { top: 700px; }

  /* Front */
  .front-brand {
    position: absolute;
    top: 120px; left: 0; right: 0;
    text-align: center;
    font-weight: 700;
    font-size: 52px;
    letter-spacing: 6px;
    color: var(--green);
    line-height: 1.2;
  }
  .front-brand .mark {
    display: inline-block;
    width: 18px; height: 18px;
    background: var(--blue);
    margin-right: 14px;
    vertical-align: middle;
  }
  .front-services {
    position: absolute;
    left: 0; right: 0; bottom: 36px;
    text-align: center;
    font-size: 15px;
    color: var(--white);
    letter-spacing: .3px;
  }
  .front-edge {
    position: absolute;
    left: 0; right: 0; bottom: 0;
    height: 12px;
    background: linear-gradient(90deg, var(--teal), var(--blue));
  }

  /* Back */
  .back-panel { position: absolute; inset: 0; }
  .back-brand {
    position: absolute;
    top: 34px; right: 60px;
    font-weight: 700;
    font-size: 34px;
    letter-spacing: 4px;
    color: var(--green);
  }
  .person { position: absolute; left: 40px; top: 112px; }
  .person-name {
    font-weight: 700;
    font-size: 26px;
    letter-spacing: 1px;
    text-transform: uppercase;
  }
  .person-creds { font-size: 12px; color: var(--muted); margin-top: 4px; }
  .contacts { list-style: none; margin-top: 14px; }
  .contacts li {
    display: flex; align-items: center; gap: 12px;
    font-size: 15px; line-height: 25px;
  }
  .contacts svg { width: 15px; height: 15px; fill: var(--white); flex: none; }
  .slogan {
    position: absolute;
    left: 36px; bottom: 58px;
    font-size: 16px;
    color: var(--white);
  }
  .follow {
    position: absolute;
    right: 28px; bottom: 22px;
    display: flex; align-items: center; gap: 8px;
    font-size: 14px; color: var(--blue);
  }
  .follow .dot {
    width: 20px; height: 20px; border-radius: 50%;
  }
  .dot--a { background: #3d9be9; }
  .dot--b { background: #c2357e; }
</style>
</head>
<body>

<section class="card card--front" aria-label="Card front">
  <div class="front-brand"><span class="mark"></span>VANTE PHYSIO</div>
  <p class="front-services">Direct Billing | Services Including Physiotherapy | IMS | Acupuncture</p>
  <div class="front-edge"></div>
</section>

<section class="card card--back" aria-label="Card back">
  <svg class="back-panel" viewBox="0 0 640 370" aria-hidden="true">
    <defs>
      <linearGradient id="panelFill" x1="0" y1="0" x2="1" y2="0">
        <stop offset="0" stop-color="#2b5889"/>
        <stop offset="1" stop-color="#1a5a4c"/>
      </linearGradient>
    </defs>
    <polygon points="0,100 330,100 470,175 420,200 250,270 0,270" fill="url(#panelFill)"/>
    <polygon points="250,270 520,180 640,230 640,255 300,275" fill="#2b5889" opacity=".85"/>
  </svg>

  <div class="back-brand">VANTE PHYSIO</div>

  <div class="person">
    <h1 class="person-name">Gil Varney</h1>
    <p class="person-creds">BSc(kin), MPT, CAFCI, IMS</p>
    <ul class="contacts">
      <li><svg viewBox="0 0 16 16"><path d="M3 1h3l1.5 4-2 1.5a9 9 0 0 0 4 4L11 8.5l4 1.5v3a2 2 0 0 1-2 2A12 12 0 0 1 1 3a2 2 0 0 1 2-2z"/></svg>867-412-5093</li>
      <li><svg viewBox="0 0 16 16"><path d="M1 3h14v10H1zM2 4l6 5 6-5v-.2H2z" fill-rule="evenodd"/></svg>VantePhysio@mailbox-demo.ca</li>
      <li><svg viewBox="0 0 16 16"><path d="M8 1a7 7 0 1 0 0 14A7 7 0 0 0 8 1zm0 1.3c.8.8 1.5 2.3 1.7 4.2H6.3C6.5 4.6 7.2 3.1 8 2.3zM2.4 7.5h2.6c.1 2 .6 3.6 1.3 4.8A5.7 5.7 0 0 1 2.4 7.5zm4 0h3.2C9.5 9.6 8.9 11.2 8 12.3 7.1 11.2 6.5 9.6 6.4 7.5zm4.6 0h2.6a5.7 5.7 0 0 1-3.9 4.8c.7-1.2 1.2-2.8 1.3-4.8zM2.4 6.5A5.7 5.7 0 0 1 6.3 2c-.7 1.2-1.2 2.7-1.3 4.5zm8.6 0c-.1-1.8-.6-3.3-1.3-4.5a5.7 5.7 0 0 1 3.9 4.5z"/></svg>www.VantePhysio.ca</li>
    </ul>
  </div>

  <p class="slogan">Mobile Physiotherapy - Your Road To Recovery</p>

  <div class="follow">
    <span>Follow us on:</span>
    <span class="dot dot--a"></span>
    <span class="dot dot--b"></span>
  </div>
</section>

</body>
</html>
```